4 Page Music Brochure design

We need assistance in designing a 4 Page A4 (A3 folded) Brochure promoting International Music Tour options for school groups. We have included text in the brief as well as images to be used in the brochure.

```html
<!DOCTYPE html>
<html lang="en">
<head>
<meta charset="utf-8">
<title>Skyline Group Travel – Music Tours Brochure</title>
<link rel="stylesheet" href="https://fonts.googleapis.com/css2?family=Open+Sans:wght@400;600;700;800&display=swap">
<style>
  :root {
    --red: #c4161c;
    --red-deep: #8e0f13;
    --pill: #8d8d8d;
    --paper: #ffffff;
    --paper-shade: #e2e2e2;
    --backdrop: #e8e8e8;
    --ink: #5a5a5a;
    --ink-soft: #8a8a8a;
    --white: #ffffff;
  }
  * { box-sizing: border-box; margin: 0; padding: 0; }
  html, body {
    width: 1200px; height: 2525px; overflow: hidden;
    background: var(--backdrop);
    font-family: "Open Sans", Arial, sans-serif;
    color: var(--ink);
  }
  .shared-defs { position: absolute; width: 0; height: 0; }
  .canvas { position: relative; width: 1200px; height: 2525px; }

  .page {
    position: absolute; width: 500px; height: 707px;
    background: var(--paper); overflow: hidden;
    box-shadow: 0 6px 18px rgba(0,0,0,.16);
  }
  .page-art { position: absolute; inset: 0; width: 500px; height: 707px; }

  .cover-solo   { left: 350px; top: 90px; }
  .back-cover   { left: 100px; top: 909px; }
  .front-cover  { left: 600px; top: 909px; }
  .inside-left  { left: 100px; top: 1728px; }
  .inside-right { left: 600px; top: 1728px; }

  /* brand name */
  .brand {
    position: absolute; display: flex; align-items: center; gap: 10px;
    color: var(--red); font-weight: 800; line-height: .92; text-transform: uppercase;
  }
  .brand-dot { width: 16px; height: 16px; border-radius: 50%; background: var(--red); flex: none; }
  .brand-name { font-size: 44px; letter-spacing: -1px; }
  .brand-name small { display: block; font-size: 30px; letter-spacing: -.5px; }

  .web-pill {
    position: absolute; height: 24px; border-radius: 12px;
    background: var(--pill); color: var(--white);
    font-size: 12px; font-weight: 600; letter-spacing: .5px;
    display: flex; align-items: center; justify-content: center;
  }

  .cover-tagline {
    position: absolute; left: 38px; top: 42px;
    color: var(--white); font-weight: 800; font-size: 27px; letter-spacing: .3px;
    text-shadow: 0 1px 3px rgba(0,0,0,.35);
  }

  .front .brand { left: 112px; top: 528px; }
  .front .web-pill { left: 150px; top: 638px; width: 200px; }

  .back .brand { left: 40px; top: 520px; }
  .back .brand-name { font-size: 38px; }
  .back .brand-name small { font-size: 26px; }
  .back-contact {
    position: absolute; left: 300px; top: 528px;
    font-size: 10px; line-height: 1.55; color: var(--ink);
  }
  .back .web-pill { left: 60px; top: 640px; width: 210px; }

  /* inside left */
  .spread-heading {
    position: absolute; left: 26px; top: 34px; width: 200px;
    color: var(--red); font-weight: 800; font-size: 16px; line-height: 1.2; text-transform: uppercase;
  }
  .inside-left .brand { left: 28px; top: 372px; }
  .inside-left .brand-name { font-size: 32px; }
  .inside-left .brand-name small { font-size: 22px; }
  .intro-copy {
    position: absolute; left: 28px; top: 450px; width: 205px;
    font-size: 8.6px; line-height: 1.5; color: var(--ink);
  }
  .intro-copy p { margin-bottom: 8px; }
  .intro-copy .lead { color: var(--red); font-weight: 600; }
  .services {
    position: absolute; left: 258px; top: 372px; width: 215px;
  }
  .services h3 { font-size: 9.5px; font-weight: 700; color: var(--red); margin-bottom: 7px; text-transform: uppercase; }
  .services ul { list-style: none; }
  .services li {
    display: flex; gap: 7px; align-items: flex-start;
    font-size: 8.6px; line-height: 1.35; margin-bottom: 5px; color: var(--ink);
  }
  .services li::before {
    content: ""; width: 7px; height: 7px; margin-top: 2px; flex: none;
    border: 1.5px solid var(--red); border-radius: 1px;
  }

  /* inside right */
  .tour-list { position: absolute; left: 28px; top: 292px; width: 448px; }
  .tour {
    display: flex; gap: 14px; height: 72px; align-items: flex-start;
  }
  .tour-thumb { width: 72px; height: 52px; flex: none; }
  .tour h4 { font-size: 10.5px; font-weight: 700; color: var(--red); margin-bottom: 3px; }
  .tour p { font-size: 8.3px; line-height: 1.45; color: var(--ink); }
</style>
</head>
<body>

<svg class="shared-defs" aria-hidden="true">
  <defs>
    <linearGradient id="sunsetSky" x1="0" y1="0" x2="0" y2="1">
      <stop offset="0" stop-color="#9a8a3c"/>
      <stop offset=".18" stop-color="#eeb135"/>
      <stop offset=".34" stop-color="#d8772c"/>
      <stop offset=".52" stop-color="#4e5a78"/>
      <stop offset="1" stop-color="#1d2744"/>
    </linearGradient>
    <linearGradient id="planeSky" x1="0" y1="0" x2="1" y2="1">
      <stop offset="0" stop-color="#2f4d80"/>
      <stop offset=".45" stop-color="#7891b0"/>
      <stop offset=".7" stop-color="#d99a4a"/>
      <stop offset="1" stop-color="#30405e"/>
    </linearGradient>
    <linearGradient id="redBand" x1="0" y1="0" x2="1" y2="0">
      <stop offset="0" stop-color="#8e0f13"/>
      <stop offset=".5" stop-color="#c4161c"/>
      <stop offset="1" stop-color="#a91217"/>
    </linearGradient>
    <linearGradient id="paperFade" x1="0" y1="0" x2="0" y2="1">
      <stop offset="0" stop-color="#ffffff"/>
      <stop offset=".75" stop-color="#f1f1f1"/>
      <stop offset="1" stop-color="#d9d9d9"/>
    </linearGradient>
    <linearGradient id="cityHaze" x1="0" y1="0" x2="0" y2="1">
      <stop offset="0" stop-color="#dfe5ea"/>
      <stop offset=".6" stop-color="#a9b3bd"/>
      <stop offset="1" stop-color="#7d8793"/>
    </linearGradient>
    <linearGradient id="canalDusk" x1="0" y1="0" x2="0" y2="1">
      <stop offset="0" stop-color="#8f8ea8"/>
      <stop offset=".5" stop-color="#c59a7e"/>
      <stop offset="1" stop-color="#6d5f5a"/>
    </linearGradient>
  </defs>
</svg>

<main class="canvas">

  <!-- Front cover, single view -->
  <section class="page front cover-solo">
    <svg class="page-art" viewBox="0 0 500 707" aria-hidden="false">
      <rect width="500" height="707" fill="url(#paperFade)"/>
      <path role="img" aria-label="Photo: students with luggage walking to an aircraft on the apron at sunset" d="M0 0H500V300C410 390 230 440 0 420Z" fill="url(#sunsetSky)"/>
      <path d="M0 420C230 440 410 390 500 300V352C420 452 240 492 0 472Z" fill="url(#redBand)"/>
      <path d="M0 472C240 492 420 452 500 352V364C420 466 240 506 0 486Z" fill="#d4d4d4"/>
    </svg>
    <h2 class="cover-tagline">EXPERIENCES FOR LIFE</h2>
    <div class="brand"><span class="brand-dot"></span><span class="brand-name">Skyline<small>Group Travel</small></span></div>
    <div class="web-pill">www.skylinegroup.travel</div>
  </section>

  <!-- Outer spread: back cover -->
  <section class="page back back-cover">
    <svg class="page-art" viewBox="0 0 500 707">
      <rect width="500" height="707" fill="url(#paperFade)"/>
      <path role="img" aria-label="Photo: side of a passenger aircraft at the gate under an evening sky" d="M0 0H500V420C270 440 90 390 0 300Z" fill="url(#planeSky)"/>
      <path d="M0 300C90 390 270 440 500 420V472C260 492 80 452 0 352Z" fill="url(#redBand)"/>
      <path d="M0 352C80 452 260 492 500 472V486C260 506 80 466 0 364Z" fill="#d4d4d4"/>
      <rect role="img" aria-label="Faint world map" x="20" y="495" width="280" height="150" rx="6" fill="#d6d6d6" opacity=".55"/>
    </svg>
    <div class="brand"><span class="brand-dot"></span><span class="brand-name">Skyline<small>Group Travel</small></span></div>
    <address class="back-contact">hello@skylinegroup.travel<br>02 5550 1480<br>PO Box 210, Riverton</address>
    <div class="web-pill">www.skylinegroup.travel</div>
  </section>

  <!-- Outer spread: front cover -->
  <section class="page front front-cover">
    <svg class="page-art" viewBox="0 0 500 707">
      <rect width="500" height="707" fill="url(#paperFade)"/>
      <path role="img" aria-label="Photo: students with luggage walking to an aircraft on the apron at sunset" d="M0 0H500V300C410 390 230 440 0 420Z" fill="url(#sunsetSky)"/>
      <path d="M0 420C230 440 410 390 500 300V352C420 452 240 492 0 472Z" fill="url(#redBand)"/>
      <path d="M0 472C240 492 420 452 500 352V364C420 466 240 506 0 486Z" fill="#d4d4d4"/>
    </svg>
    <h2 class="cover-tagline">EXPERIENCES FOR LIFE</h2>
    <div class="brand"><span class="brand-dot"></span><span class="brand-name">Skyline<small>Group Travel</small></span></div>
    <div class="web-pill">www.skylinegroup.travel</div>
  </section>

  <!-- Inside spread: left page -->
  <section class="page inside-left">
    <svg class="page-art" viewBox="0 0 500 707">
      <rect width="500" height="707" fill="#ffffff"/>
      <path role="img" aria-label="Photo: city skyline in daytime haze" d="M0 0H500V250C380 320 200 345 0 330Z" fill="url(#cityHaze)"/>
      <path role="img" aria-label="Photo: student filming with a video camera" d="M240 0H500V250C440 285 360 305 240 318Z" fill="#8697ab"/>
      <circle role="img" aria-label="Round photo: temple gate" cx="300" cy="270" r="34" fill="#c4745b" stroke="#ffffff" stroke-width="4"/>
      <circle role="img" aria-label="Round photo: travellers sightseeing" cx="348" cy="228" r="26" fill="#9aa4ae" stroke="#ffffff" stroke-width="4"/>
      <path d="M0 330C200 345 380 320 500 250V290C380 360 200 380 0 360Z" fill="url(#redBand)"/>
      <path d="M0 360C200 380 380 360 500 290V298C380 370 200 390 0 370Z" fill="#d4d4d4"/>
      <path d="M0 678C180 668 360 672 500 660V707H0Z" fill="url(#redBand)"/>
    </svg>
    <h2 class="spread-heading">Making overseas school tours accessible to all students</h2>
    <div class="brand"><span class="brand-dot"></span><span class="brand-name">Skyline<small>Group Travel</small></span></div>
    <div class="intro-copy">
      <p>Skyline Group Travel was established in 2001 to provide tours to overseas destinations.</p>
      <p class="lead">Our focus is providing unique opportunities to travel and learn, giving students the best possible experience abroad.</p>
      <p>Our understanding of the unique requirements of school groups lets us plan every detail, from flights and stays to rehearsals and concerts, so teachers can focus on their students while we handle the rest.</p>
    </div>
    <div class="services">
      <h3>We can assist in providing:</h3>
      <ul>
        <li>Customised itineraries</li>
        <li>Festival/event entry</li>
        <li>Workshops with clinicians</li>
        <li>School exchanges</li>
        <li>Public performances</li>
        <li>Transport</li>
        <li>Venue hire</li>
        <li>Trusted, quality suppliers</li>
        <li>Sightseeing</li>
        <li>Expert Guides and Tour Escorts</li>
        <li>Negotiated group discounts on airfares, accommodation, transport and activities</li>
      </ul>
    </div>
  </section>

  <!-- Inside spread: right page -->
  <section class="page inside-right">
    <svg class="page-art" viewBox="0 0 500 707">
      <rect width="500" height="707" fill="#ffffff"/>
      <path role="img" aria-label="Photo: domed church and old buildings along a canal at dusk" d="M0 0H500V200C360 250 170 265 0 250Z" fill="url(#canalDusk)"/>
      <path d="M0 250C170 265 360 250 500 200V232C360 285 170 296 0 278Z" fill="url(#redBand)"/>
      <path d="M0 278C170 296 360 285 500 232V240C360 294 170 305 0 286Z" fill="#d4d4d4"/>
      <path d="M0 660C140 672 320 668 500 678V707H0Z" fill="url(#redBand)"/>
    </svg>
    <div class="tour-list">
      <article class="tour">
        <svg class="tour-thumb" viewBox="0 0 72 52"><rect role="img" aria-label="Photo: choir festival city view" width="72" height="52" fill="#5e6c86"/></svg>
        <div><h4>International Choral Festival (5th to the 15th of July 2020)</h4>
        <p>Join choirs from around the world for ten days of competitions, workshops and shared concerts. We arrange entry, accommodation, transport and rehearsal space for your whole group.</p></div>
      </article>
      <article class="tour">
        <svg class="tour-thumb" viewBox="0 0 72 52"><rect role="img" aria-label="Photo: concert hall interior" width="72" height="52" fill="#8a4a2c"/></svg>
        <div><h4>Grand Concert Hall</h4>
        <p>Perform on one of the world's great stages. Our packages include venue booking, a professional recording of your concert and guided visits across the city.</p></div>
      </article>
      <article class="tour">
        <svg class="tour-thumb" viewBox="0 0 72 52"><rect role="img" aria-label="Photo: red stage curtains" width="72" height="52" fill="#a8241e"/></svg>
        <div><h4>Japan Music Tours</h4>
        <p>Discover traditional and modern music in Tokyo and Kyoto, with drumming workshops, school exchanges and joint performances with local students.</p></div>
      </article>
      <article class="tour">
        <svg class="tour-thumb" viewBox="0 0 72 52"><rect role="img" aria-label="Photo: ornate opera house interior" width="72" height="52" fill="#9a6a32"/></svg>
        <div><h4>European Instrumental Tours</h4>
        <p>Travel through Vienna, Salzburg and Prague, performing in historic halls and churches while learning from leading instrumental teachers.</p></div>
      </article>
      <article class="tour">
        <svg class="tour-thumb" viewBox="0 0 72 52"><rect role="img" aria-label="Photo: student choir performing" width="72" height="52" fill="#7a3a3a"/></svg>
        <div><h4>US Music Road Trip</h4>
        <p>From Nashville to New Orleans, explore the roots of American music with live shows, studio visits and performance opportunities along the way.</p></div>
      </article>
    </div>
  </section>

</main>
</body>
</html>
```